Creative Business Card for my Sail Boat.. Tide & Time

Going to order PLASTIC business cards for my boat.. she is a sailing vessel catamaran named Tide & Time..

Target Market(s)

to impress other boaters with a unique designed plastic card

Contact Information for Business Card

S/V Tide & Time
Captain Owen Harlow
harlow@owen.example
Mobile/WhatsApp 1-555-318-7062
www.sailtideandtime.example

Requirements
Must have
• Cool colors. logo.. and info in Business Card Details.. Thanks! Utilize clear or cloudy plastic in design. Thanks

```html
<!DOCTYPE html>
<html lang="en">
<head>
<meta charset="utf-8">
<title>Tide &amp; Time — Business Card</title>
<link rel="stylesheet" href="https://fonts.googleapis.com/css2?family=Roboto:wght@400;700&display=swap">
<style>
  :root {
    --backdrop: #e7e3de;
    --card-frost: #f3f2ef;
    --card-edge: #ffffff;
    --ink-brown: #5a3a2c;
    --ink-text: #4a4440;
    --logo-ink: #6e625a;
    --peace-green: #2f8a3a;
    --heart-red: #b3232a;
  }
  * { margin: 0; padding: 0; box-sizing: border-box; }
  html, body {
    width: 1200px; height: 1200px; overflow: hidden;
    background: var(--backdrop);
    font-family: "Roboto", Arial, sans-serif;
  }
  .canvas { position: relative; width: 1200px; height: 1200px; }
  .card {
    position: absolute; left: 60px; top: 306px;
    width: 1080px; height: 588px;
    border-radius: 30px;
    background: linear-gradient(135deg, rgba(255,255,255,0.85), var(--card-frost));
    border: 2px solid var(--card-edge);
    box-shadow: 0 18px 40px rgba(70,55,45,0.15);
    overflow: hidden;
  }
  .card-decor { position: absolute; inset: 0; width: 100%; height: 100%; }
  .brand {
    position: absolute; left: 62px; top: 46px;
    display: flex; align-items: center; gap: 26px;
  }
  .brand-name {
    font-weight: 700; font-size: 92px; line-height: 98px;
    color: var(--logo-ink); letter-spacing: -1px;
  }
  .brand-dot {
    width: 62px; height: 62px; border-radius: 50%;
    border: 7px solid var(--peace-green);
    align-self: flex-start; margin-top: 22px;
  }
  .captain {
    position: absolute; left: 56px; top: 320px;
    font-weight: 700; font-size: 32px; color: var(--ink-brown);
    letter-spacing: 0.3px;
  }
  .contact {
    position: absolute; left: 56px; top: 420px;
    list-style: none; font-size: 27px; color: var(--ink-text);
    line-height: 41px;
  }
  .contact-phone { display: flex; align-items: center; gap: 12px; }
  .icon-mobile { width: 18px; height: 26px; }
</style>
</head>
<body>
<main class="canvas">
  <section class="card" aria-label="Tide &amp; Time business card">
    <svg class="card-decor" viewBox="0 0 1080 588" aria-hidden="true">
      <circle cx="916" cy="159" r="142" fill="none" stroke="var(--peace-green)" stroke-width="27"/>
      <circle cx="945" cy="470" r="128" fill="none" stroke="var(--heart-red)" stroke-width="25"/>
    </svg>

    <div class="brand">
      <span class="brand-name">Tide &amp;<br>Time</span>
      <span class="brand-dot"></span>
    </div>

    <h1 class="captain">CAPTAIN OWEN HARLOW</h1>

    <ul class="contact">
      <li class="contact-phone">1-555-318-7062
        <svg class="icon-mobile" viewBox="0 0 18 26" aria-label="Mobile">
          <rect x="1.5" y="1.5" width="15" height="23" rx="3" fill="none" stroke="var(--peace-green)" stroke-width="2.5"/>
          <line x1="7" y1="20" x2="11" y2="20" stroke="var(--peace-green)" stroke-width="2.5" stroke-linecap="round"/>
        </svg>
      </li>
      <li class="contact-email">harlow@owen.example</li>
      <li class="contact-web">www.sailtideandtime.example</li>
    </ul>
  </section>
</main>
</body>
</html>
```